Emerging jewellery maker and designer needs a business card design with logo

I need a business card to hand to industry officials and potential clients. I handmake my own jewellery that targets mostly females from 20 to 50 years of age. I use mostly sterling silver, with some gemstones and often have tribal or geometric elements in the design. The final design should communicate originality, simplicity and memorability.

Target Market(s)

20- 50 year old females

Industry/Entity Type

Business

Contact Information for Business Card

Title: Marisol Quenton Designs
Tagline: Jewellery and Object maker
Contact details:
-email: kmquenton4@mailvora.com
-instagram: @marisolquenton
-Mobile: 047-612-5093

Requirements
Must have
• Clear and strong design aesthetic
Nice to have
• I like symbols and use tribal and geometric symbols in my work. If this could be incorporated that would be great.( ideally a way better/digital version of the uploaded image could act as a logo of sorts)
Should not have
• Tacky sayings or quotes, misleading images, or an literal images of diamonds, rings etc

```html
<!DOCTYPE html>
<html lang="en">
<head>
<meta charset="utf-8">
<title>Marisol Quenton Designs – Business Card</title>
<link href="https://fonts.googleapis.com/css2?family=Cinzel:wght@400;600&family=Special+Elite&display=swap" rel="stylesheet">
<style>
  :root {
    --page-bg: #e9e6df;
    --navy-deep: #0d2447;
    --navy-mid: #1b4478;
    --navy-light: #2c5f99;
    --aqua: #2fa3d6;
    --aqua-light: #6fd0f2;
    --aqua-pale: #b6ecfb;
    --silver: #dfe7ef;
    --white: #ffffff;
  }
  * { box-sizing: border-box; margin: 0; padding: 0; }
  html, body {
    width: 841px; height: 1200px; overflow: hidden;
    background: var(--page-bg);
  }
  .canvas {
    position: relative; width: 841px; height: 1200px;
    display: flex; flex-direction: column; align-items: center; justify-content: center;
    gap: 90px;
  }
  .card {
    position: relative; width: 700px; height: 400px; overflow: hidden;
    background: linear-gradient(160deg, var(--navy-mid) 0%, var(--navy-deep) 70%);
    box-shadow: 0 10px 26px rgba(0,0,0,0.22);
  }
  .card__waves { position: absolute; inset: 0; width: 100%; height: 100%; }
  .brand-mark {
    position: absolute; display: flex; align-items: center; gap: 10px;
  }
  .brand-mark__circle {
    width: 46px; height: 46px; border-radius: 50%;
    background: var(--aqua);
  }
  .brand-mark__name {
    font-family: "Cinzel", serif; font-weight: 600; font-size: 16px;
    color: var(--silver); letter-spacing: 1px; white-space: nowrap;
  }
  .identity { position: absolute; white-space: nowrap; }
  .business-name {
    font-family: "Cinzel", serif; font-weight: 400; font-size: 23px;
    color: var(--silver); letter-spacing: 1px;
  }
  .tagline {
    font-family: "Special Elite", monospace; font-size: 15px;
    color: var(--aqua-pale); letter-spacing: 2px; margin-top: 6px;
  }
  /* front */
  .card--front .brand-mark { left: 250px; top: 50px; }
  .card--front .identity { left: 250px; top: 140px; }
  /* back */
  .card--back .brand-mark { left: 45px; top: 150px; }
  .card--back .identity { left: 280px; top: 36px; }
  .contact-list {
    position: absolute; left: 320px; top: 135px; list-style: none;
    display: flex; flex-direction: column; gap: 18px;
  }
  .contact-list__item {
    display: flex; align-items: center; gap: 14px;
    font-family: "Special Elite", monospace; font-size: 15px; color: var(--white);
    white-space: nowrap;
  }
  .contact-list__icon { width: 22px; height: 22px; flex: none; }
</style>
</head>
<body>
<main class="canvas">

  <section class="card card--front" aria-label="Business card front">
    <svg class="card__waves" viewBox="0 0 700 400" preserveAspectRatio="none" aria-hidden="true">
      <path d="M0 400 L0 372 C250 352 480 315 700 262 L700 400 Z" fill="var(--aqua)"/>
      <path d="M0 400 L0 386 C260 368 500 332 700 290 L700 400 Z" fill="var(--navy-light)"/>
      <path d="M150 400 C360 385 540 350 700 315 L700 400 Z" fill="var(--aqua-light)" opacity="0.85"/>
      <path d="M0 368 C250 348 480 311 700 258" stroke="var(--aqua-pale)" stroke-width="2" fill="none"/>
    </svg>
    <div class="brand-mark">
      <span class="brand-mark__circle"></span>
      <span class="brand-mark__name">Marisol Quenton</span>
    </div>
    <div class="identity">
      <h1 class="business-name">Marisol Quenton Designs</h1>
      <p class="tagline">Jewellery &amp; Object Maker</p>
    </div>
  </section>

  <section class="card card--back" aria-label="Business card back">
    <svg class="card__waves" viewBox="0 0 700 400" preserveAspectRatio="none" aria-hidden="true">
      <path d="M0 400 L0 372 C250 352 480 315 700 262 L700 400 Z" fill="var(--aqua)"/>
      <path d="M0 400 L0 386 C260 368 500 332 700 290 L700 400 Z" fill="var(--navy-light)"/>
      <path d="M150 400 C360 385 540 350 700 315 L700 400 Z" fill="var(--aqua-light)" opacity="0.85"/>
      <path d="M0 368 C250 348 480 311 700 258" stroke="var(--aqua-pale)" stroke-width="2" fill="none"/>
    </svg>
    <div class="brand-mark">
      <span class="brand-mark__circle"></span>
      <span class="brand-mark__name">Marisol Quenton</span>
    </div>
    <div class="identity">
      <h2 class="business-name">Marisol Quenton Designs</h2>
      <p class="tagline">Jewellery &amp; Object Maker</p>
    </div>
    <ul class="contact-list">
      <li class="contact-list__item">
        <svg class="contact-list__icon" viewBox="0 0 24 24" aria-hidden="true">
          <rect x="2" y="5" width="20" height="14" fill="var(--white)"/>
          <path d="M2 5 L12 13 L22 5" stroke="var(--navy-mid)" stroke-width="1.6" fill="none"/>
        </svg>
        kmquenton4@mailvora.com
      </li>
      <li class="contact-list__item">
        <svg class="contact-list__icon" viewBox="0 0 24 24" aria-hidden="true">
          <rect x="3" y="3" width="18" height="18" fill="var(--white)"/>
        </svg>
        @marisolquenton
      </li>
      <li class="contact-list__item">
        <svg class="contact-list__icon" viewBox="0 0 24 24" aria-hidden="true">
          <rect x="6" y="1" width="12" height="22" rx="2" fill="var(--white)"/>
          <rect x="8" y="4" width="8" height="13" fill="var(--navy-mid)"/>
          <circle cx="12" cy="20" r="1.2" fill="var(--navy-mid)"/>
        </svg>
        047-612-5093
      </li>
    </ul>
  </section>

</main>
</body>
</html>
```